Business Card Design Project

I need a new business card design for my building/development company: Kestrel Ridge Builders.

We specialise in small sub-divisions, multi-story developments and new house builds.
We handle the whole process from concept stage right throught to a fully developed property.
Updates

Target Market(s)

people looking to develop their property and need help. New property buyers

Industry/Entity Type

House

Requirements
Must have
• My logo on both sides:
Side 1: Logo taking up whole side as per old card but with a color/style change.

Side 2: Contact page: include logo but the rest just surprise me!

All contact details will be: (and need to be changable for each employee) I'll inform you of specifics before printing.

Name Surname
Position ie. Managing director
M: insert mobile
E: insert email
P.O. Box 518, Ashwell, Vic, 3094
www.kestrelridgebuilders.com.au

Nice to have
• Colors i'd like: (not necessarily all but this is the basic idea)

Black, blue, grey, silver, white

```html
<!DOCTYPE html>
<html lang="en">
<head>
<meta charset="utf-8">
<title>Kestrel Ridge Builders – Business Card</title>
<link rel="stylesheet" href="https://fonts.googleapis.com/css2?family=Source+Sans+3:wght@400;600;700&display=swap">
<style>
  :root {
    --page: #ffffff;
    --card: #dfdfde;
    --brand-blue: #1b7cc1;
    --ink: #231f20;
    --label: #2b2b2b;
    --white: #ffffff;
    --muted: #d9d2cc;
    --timber-dark: #7e3217;
    --timber-mid: #a5461f;
    --timber-light: #b4552a;
  }
  html, body {
    margin: 0;
    padding: 0;
    width: 1200px;
    height: 456px;
    overflow: hidden;
    background: var(--page);
    font-family: "Source Sans 3", Arial, sans-serif;
    color: var(--ink);
  }
  .canvas { position: relative; width: 1200px; height: 456px; }

  .side-label {
    position: absolute;
    top: 10px;
    width: 200px;
    margin-left: -100px;
    text-align: center;
    font-size: 22px;
    color: var(--label);
  }
  .side-label--front { left: 297px; }
  .side-label--back { left: 891px; }

  .card {
    position: absolute;
    top: 47px;
    height: 348px;
    background: var(--card);
    overflow: hidden;
  }
  .card--front { left: 20px; width: 555px; }
  .card--back { left: 614px; width: 554px; }

  .timber-band {
    position: absolute;
    left: 0;
    width: 100%;
    background: linear-gradient(90deg, var(--timber-dark), var(--timber-mid) 30%, var(--timber-light) 55%, var(--timber-mid) 80%, var(--timber-dark));
  }
  .card--front .timber-band { top: 255px; height: 93px; }
  .card--back .timber-band { top: 171px; height: 95px; }

  .brand-mark {
    position: absolute;
    background: var(--brand-blue);
  }
  .card--front .brand-mark { left: 222px; top: 62px; width: 104px; height: 104px; }
  .card--back .brand-mark { left: 112px; top: 40px; width: 66px; height: 66px; }

  .brand-name {
    position: absolute;
    margin: 0;
    font-weight: 600;
    color: var(--brand-blue);
    white-space: nowrap;
    letter-spacing: -0.5px;
  }
  .brand-tagline {
    position: absolute;
    margin: 0;
    font-weight: 400;
    color: var(--ink);
    white-space: nowrap;
  }
  .card--front .brand-name {
    left: 0; width: 100%; text-align: center;
    top: 180px; font-size: 41px; line-height: 48px;
  }
  .card--front .brand-tagline {
    left: 0; width: 100%; text-align: center;
    top: 226px; font-size: 18px; line-height: 20px; letter-spacing: 1px;
  }
  .card--back .brand-name {
    left: 40px; top: 118px; font-size: 24px; line-height: 30px;
  }
  .card--back .brand-tagline {
    left: 50px; top: 145px; font-size: 11px; line-height: 13px; letter-spacing: 0.6px;
  }

  .person {
    position: absolute;
    top: 182px;
    right: 0;
    width: 178px;
    color: var(--white);
    text-align: right;
  }
  .person__name {
    margin: 0 45px 0 0;
    font-size: 20px;
    font-weight: 700;
    line-height: 26px;
  }
  .person__role {
    margin: 0 45px 0 0;
    font-size: 16px;
    line-height: 20px;
    color: var(--muted);
  }
  .person__mobile {
    margin: 5px 0 0 0;
    padding: 5px 0 0 8px;
    border-top: 1px solid var(--muted);
    text-align: left;
    font-size: 13px;
    line-height: 16px;
  }

  .contact {
    position: absolute;
    top: 278px;
    margin: 0;
    font-size: 12.5px;
    line-height: 18px;
    color: var(--ink);
    white-space: nowrap;
  }
  .contact--postal { left: 40px; }
  .contact--phone { left: 274px; }
  .contact span { display: block; }
</style>
</head>
<body>
<div class="canvas">
  <div class="side-label side-label--front">Front</div>
  <div class="side-label side-label--back">Back</div>

  <section class="card card--front">
    <div class="brand-mark" aria-hidden="true"></div>
    <h1 class="brand-name">Kestrel Ridge Builders</h1>
    <p class="brand-tagline">renovation-construction-development</p>
    <div class="timber-band" role="img" aria-label="Photograph of reddish timber planks"></div>
  </section>

  <section class="card card--back">
    <div class="brand-mark" aria-hidden="true"></div>
    <h2 class="brand-name">Kestrel Ridge Builders</h2>
    <p class="brand-tagline">renovation-construction-development</p>
    <div class="timber-band" role="img" aria-label="Photograph of reddish timber planks"></div>
    <div class="person">
      <p class="person__name">Marcus Doyle</p>
      <p class="person__role">Managing director</p>
      <p class="person__mobile">Mobile: 0412 555 019</p>
    </div>
    <p class="contact contact--postal">
      <span>P.O. Box 518, Ashwell, Vic, 3094</span>
      <span>www.kestrelridgebuilders.com.au</span>
    </p>
    <p class="contact contact--phone">
      <span>Ph/Fax :&nbsp; 08 5550 1842</span>
      <span>Email &nbsp;&nbsp;: office@kestrelridge.com.au</span>
    </p>
  </section>
</div>
</body>
</html>
```